Flyer Template Design

I have attached 4 files. I would like a design template that could be used across these documents so that they have a common look and feel. The content of the documents is tested and should not be changed significantly. The images can be changed. I have also attache our logo for color compatibility.
Updates

Need extra days to review

Target Market(s)

Wealthy Christian donors

Font styles to use
Serif
Sans Serif

```html
<!DOCTYPE html>
<html lang="en">
<head>
<meta charset="utf-8">
<title>The Final Lap</title>
<link href="https://fonts.googleapis.com/css2?family=Bodoni+Moda:ital,wght@0,500;1,500&family=Lato:wght@400&family=Roboto+Slab:wght@300;700&display=swap" rel="stylesheet">
<style>
  :root {
    --navy: #15527f;
    --navy-deep: #0d4a7a;
    --sky: #5bc0e8;
    --mist: #e6e7e9;
    --ink: #555a60;
    --white: #ffffff;
  }
  * { margin: 0; padding: 0; box-sizing: border-box; }
  html, body { width: 902px; height: 1200px; overflow: hidden; background: var(--white); }
  .flyer { position: relative; width: 902px; height: 1200px; background: var(--white); font-family: "Lato", sans-serif; color: var(--ink); }
  .abs { position: absolute; }

  .intro-frame { left: 38px; top: 180px; width: 829px; height: 163px; border: 5px solid var(--navy); }
  .intro-photo { left: 80px; top: 0; width: 305px; height: 378px; background: linear-gradient(170deg, #14294f 0%, #1c3a68 45%, #1f4f7d 75%, #27517e 100%); }
  .title { left: 423px; top: 60px; font-family: "Roboto Slab", serif; line-height: 1; }
  .title-the { display: block; font-weight: 700; font-size: 48px; color: var(--navy-deep); }
  .title-lap { display: block; font-weight: 300; font-size: 62px; color: var(--sky); margin-top: 2px; letter-spacing: 0.5px; }
  .intro-text { left: 423px; top: 199px; width: 400px; }

  .finish-band { left: 0; top: 378px; width: 902px; height: 361px; background: var(--mist); }
  .section-head { font-family: "Bodoni Moda", serif; font-weight: 500; font-size: 17.5px; color: var(--navy-deep); letter-spacing: 0.2px; }
  .body-text { font-size: 12.8px; line-height: 15.5px; }
  .pull { font-family: "Bodoni Moda", serif; font-weight: 500; font-size: 17px; line-height: 22px; color: var(--navy-deep); }

  .finish-head { left: 79px; top: 418px; }
  .finish-quote { left: 79px; top: 455px; width: 780px; }
  .finish-question { left: 79px; top: 513px; }
  .finish-nations { left: 79px; top: 577px; width: 780px; }
  .finish-lap { left: 79px; top: 683px; }

  .sprint-photo { left: 453px; top: 739px; width: 449px; height: 461px; background: linear-gradient(180deg, #2a3f86 0%, #3d4da0 40%, #3f5e9a 68%, #3e6b4f 82%, #2f4a78 100%); }
  .sprint-callout { left: 453px; top: 978px; width: 449px; text-align: center; font-family: "Roboto Slab", serif; font-weight: 700; font-size: 33px; line-height: 34px; color: var(--white); }
  .sprint-head { left: 79px; top: 771px; }
  .sprint-peter { left: 79px; top: 810px; width: 350px; }
  .sprint-partner { left: 79px; top: 895px; width: 325px; }
  .sprint-join { left: 79px; top: 1022px; font-style: italic; font-size: 20px; line-height: 24px; }

  .contact-band { left: 0; top: 1130px; width: 902px; height: 40px; background: var(--navy-deep); color: var(--white); font-family: "Bodoni Moda", serif; font-weight: 500; font-size: 16.5px; line-height: 40px; text-align: center; }
</style>
</head>
<body>
<main class="flyer">
  <div class="abs intro-frame"></div>
  <div class="abs intro-photo" role="img" aria-label="Photo of relay sprinters racing toward the finish on a stadium track, toned in deep blue"></div>
  <h1 class="abs title"><span class="title-the">THE</span><span class="title-lap">FINAL LAP</span></h1>
  <p class="abs body-text intro-text">Every four years, the great Marathon is run through the streets of the host city. The final lap, though, is always run in the main Stadium. At the end of the race, the runners burst into the stadium for the final lap, and the crowd explodes in celebration of a long race well run. For 2000 years, the church has been running a Marathon, racing to fulfill Jesus’ command to “make disciples of all nations.” But now we’re nearly done: we’ve come into the stadium; we’re on the final lap. And the heavenly crowd is standing and cheering!</p>

  <section class="abs finish-band"></section>
  <h2 class="abs section-head finish-head">THE FINISH LINE</h2>
  <p class="abs body-text finish-quote">Jesus himself defined the finish line when he said, “This gospel of the kingdom will be preached in the whole world as a testimony to all nations, and then the end will come.”</p>
  <p class="abs pull finish-question">When will the race end?<br>Jesus said, when the gospel has been proclaimed to “all nations.”</p>
  <p class="abs body-text finish-nations">In the Bible, the word “nations” refers to people groups: groups of people who share a common ethnicity, culture, and language. Amazingly, there are about 12,000 of these “nations” around the world—and Jesus commanded us to make disciples in all of them! Today, there are still about 500 people groups around the world have never heard the gospel. Most of these remaining groups are small and located in remote, difficult places. But now that we know who and where they are, by God’s grace it is possible for us to engage every one of them with the gospel within the next 3 years.</p>
  <p class="abs pull finish-lap">In other words, after a long race, we’re on the final lap!</p>

  <div class="abs sprint-photo" role="img" aria-label="Photo of a sprinter leaning through the finish tape on a track"></div>
  <p class="abs sprint-callout">YOU CAN BE<br>PART OF THE<br>SPRINT TO THE<br>FINISH.</p>
  <h2 class="abs section-head sprint-head">SPRINTING TO THE FINISH</h2>
  <p class="abs body-text sprint-peter">In his second letter, the Apostle Peter instructs believers “to hasten the coming of the day of God.” As the end of the race draws near, he’s saying, we should sprint toward the finish line, striving to finish the race as quickly as we can.</p>
  <p class="abs body-text sprint-partner">Partner with the Harvest Line Fund and finance the missionaries who are taking the gospel for the first time to those last remaining people groups. Your investment will “hasten the coming of the day of God” by accelerating the effort to make “disciples in every nation.” In 2018, our partners helped take the gospel to 231 people groups in 35 countries.</p>
  <p class="abs pull sprint-join">Join us as we invest to make<br>disciples in “all nations” by 2022.</p>

  <footer class="abs contact-band">To learn more, email Martin Hale at mhale@harvestlinefund.org.</footer>
</main>
</body>
</html>
```